New Infusion Pharmacy needs Business Card design

Hello!

We are Verant Infusion Pharmacy, are we are looking for a two sided, clean and modern business card.

First, let me give you a little bit about what an infusion pharmacy does...
We compound and fill prescriptions for drugs that are injectable, meaning that they are administered via an IV bag or a syringe. Basically anything that is too advanced for a normal pill pharmacy to fill. We compound everything in our state of the art clean room, then deliver it directly to the patients home. We have an outside sales force that markets to hospitals, home health agencies, and doctor's offices.

as for the business card...
We are looking for a clean, modern card. our colors are in our logo, kind of a light bule and a darker blue. We do really like the rounded corners on the card. Also, we would like the back of the card to be the reverse colors of the front, for example, if the front of the card has a light background, then the back of the card will have a dark background.

On the back side of the card we want to have our logo, then list some of the services we offer:
-IVIG
-TPN
-Enteral Nutrition
-IV Antibiotics
-IV Hydration
-Blood Factors
-Chemotherapy
-Pain Management

Our logo is uploaded in .psd format, if you need a different format let me know and i'll throw it up here.

Thank you so much!!

Industry/Entity Type

Pharmacy

Requirements
Must have
• Front of Card: (no particular order, please arrange in whatever way you think looks best!)
-Employee Name
-Title
-Office Phone #
-Cell Phone #
-Fax #
-email address - marlo@verantcareinfuse.com
-office address - 4127 Delmore St. Larkfield, CA 92514
-Web Site - www.verantcareinfuse.com

```html
<!DOCTYPE html>
<html lang="en">
<head>
<meta charset="utf-8">
<title>Verant Infusion Pharmacy – Business Card</title>
<link rel="stylesheet" href="https://fonts.googleapis.com/css2?family=Questrial&family=Arimo:wght@400;700&family=Open+Sans:wght@400;700&display=swap">
<style>
  :root {
    --teal-dark: #0a566e;
    --paper: #ffffff;
    --ink: #2b2b2b;
    --backdrop: #e9ecee;
    --faint: rgba(255,255,255,0.08);
  }
  * { box-sizing: border-box; margin: 0; padding: 0; }
  html, body { width: 1200px; height: 706px; overflow: hidden; }
  body {
    background: var(--backdrop);
    position: relative;
    font-family: "Arimo", Arial, sans-serif;
  }
  .card {
    position: absolute;
    top: 193px;
    width: 540px;
    height: 320px;
    border-radius: 24px;
    overflow: hidden;
    box-shadow: 0 6px 18px rgba(0,0,0,0.18);
  }
  /* Front */
  .card-front { left: 40px; background: var(--paper); }
  .brand {
    position: absolute;
    left: 66px;
    top: 40px;
    color: var(--teal-dark);
    font-family: "Questrial", sans-serif;
    font-weight: 400;
  }
  .brand-name { display: block; font-size: 96px; line-height: 0.9; letter-spacing: 3px; }
  .brand-line { display: block; font-size: 19px; letter-spacing: 8px; margin-top: 10px; padding-left: 6px; }
  .contact-band {
    position: absolute;
    left: 0; right: 0;
    top: 184px;
    height: 86px;
    background: var(--teal-dark);
    color: var(--paper);
  }
  .person {
    position: absolute;
    right: 300px;
    top: 22px;
    text-align: right;
  }
  .person-name { font-size: 20px; font-weight: 700; }
  .person-title { font-size: 12px; margin-top: 2px; }
  .divider {
    position: absolute;
    left: 254px;
    top: 10px;
    width: 1px;
    height: 66px;
    background: var(--paper);
  }
  .contact-list {
    position: absolute;
    left: 266px;
    top: 8px;
    list-style: none;
    font-size: 13px;
    line-height: 17.5px;
  }
  .contact-list li { display: flex; align-items: center; gap: 6px; }
  .contact-list svg { width: 11px; height: 11px; fill: var(--paper); }
  .address {
    position: absolute;
    left: 0; right: 0;
    bottom: 16px;
    text-align: center;
    font-size: 14px;
    letter-spacing: 2.4px;
    color: var(--ink);
  }
  /* Back */
  .card-back {
    left: 620px;
    background: var(--teal-dark);
    color: var(--paper);
    font-family: "Open Sans", sans-serif;
  }
  .faint-name {
    position: absolute;
    right: -10px;
    top: 70px;
    font-family: "Questrial", sans-serif;
    font-size: 120px;
    color: var(--faint);
    letter-spacing: 2px;
  }
  .services-title {
    position: absolute;
    left: 50px;
    top: 48px;
    font-size: 26px;
    font-weight: 700;
  }
  .services {
    position: absolute;
    left: 50px;
    top: 100px;
    font-size: 19px;
    line-height: 31px;
    list-style: none;
  }
  .website {
    position: absolute;
    left: 0; right: 0;
    bottom: 40px;
    text-align: center;
    font-size: 15px;
    letter-spacing: 5px;
  }
</style>
</head>
<body>
  <section class="card card-front">
    <div class="brand">
      <span class="brand-name">VERANT</span>
      <span class="brand-line">INFUSION PHARMACY</span>
    </div>
    <div class="contact-band">
      <div class="person">
        <p class="person-name">Employee Name</p>
        <p class="person-title">Title</p>
      </div>
      <div class="divider"></div>
      <ul class="contact-list">
        <li><svg viewBox="0 0 24 24" aria-hidden="true"><path d="M6.6 10.8a15 15 0 0 0 6.6 6.6l2.2-2.2c.3-.3.7-.4 1-.2 1.1.4 2.3.6 3.6.6.6 0 1 .4 1 1V20c0 .6-.4 1-1 1A17 17 0 0 1 3 4c0-.6.4-1 1-1h3.5c.6 0 1 .4 1 1 0 1.3.2 2.5.6 3.6.1.3 0 .7-.2 1z"/></svg>0912 408375</li>
        <li><svg viewBox="0 0 24 24" aria-hidden="true"><path d="M7 1h10a2 2 0 0 1 2 2v18a2 2 0 0 1-2 2H7a2 2 0 0 1-2-2V3a2 2 0 0 1 2-2zm0 4v13h10V5z"/></svg>0912 408375</li>
        <li><svg viewBox="0 0 24 24" aria-hidden="true"><path d="M6 2h9l3 3v5H6zM3 11h18a1 1 0 0 1 1 1v8a1 1 0 0 1-1 1H3a1 1 0 0 1-1-1v-8a1 1 0 0 1 1-1z"/></svg>0912 408375</li>
        <li><svg viewBox="0 0 24 24" aria-hidden="true"><path d="M2 5h20v14H2zm2 2v.5l8 5 8-5V7z"/></svg>marlo@verantcareinfuse.com</li>
      </ul>
    </div>
    <p class="address">4127 Delmore St. Larkfield, CA 92514</p>
  </section>

  <section class="card card-back">
    <span class="faint-name" aria-hidden="true">VERANT</span>
    <h2 class="services-title">Our Services</h2>
    <ul class="services">
      <li>• IVIG &nbsp;• TPN &nbsp;• Enteral Nutrition</li>
      <li>• IV Antibiotics &nbsp;• IV Hydration</li>
      <li>• Blood Factors &nbsp;• Chemotherapy &nbsp;• Pain Management</li>
    </ul>
    <p class="website">www.verantcareinfuse.com</p>
  </section>
</body>
</html>
```